Powerpoint template for corporate presentations

Our company, ClinicMeadowlane, has recently undertaken a re-branding overhaul for our website and corporate materials (color scheme, letterhead, biz cards). In support of this re-branding effort, we need a powerpoint template for corporate presentations that will reflect the look and feel of the website.

We would like to receive a powerpoint template that contains the following slide layouts:
- title slide
- section header slide
- content slide (title & content)
- closing/acknowledgement slide

The website design, colors, fonts and images are included as attachments for your reference.An example powerpoint template is included, if needed for your reference. We would like to see the icons and colors used to make the presentation more visually appealing.

Specific comments regarding the example ppt with content attached to this brief:
- the content slides seem a bit sparse and do not have much space for text/charts.
- For the content slides, a white/light background and dark text is still expected.
- For the section header and closing slides, we would like to see a layout more engaging than just the blue background. Note: a blue or colored background is acceptable for these slides so long as the text color has enough contrast to be visible.

Industry/Entity Type

It Company

```html
<!DOCTYPE html>
<html lang="en">
<head>
<meta charset="utf-8">
<title>ClinicMeadowlane presentation template</title>
<link rel="stylesheet" href="https://fonts.googleapis.com/css2?family=Arimo:ital,wght@0,400;0,700;1,700&family=Source+Sans+3:wght@400&display=swap">
<style>
  :root {
    --page: #eceae6;
    --white: #ffffff;
    --ink: #4d4f53;
    --ink-soft: #5d6065;
    --cyan: #1eb1df;
    --cyan-deep: #1592c0;
    --slate: #51565c;
    --yellow: #fbec86;
    --yellow-edge: #e9d35a;
    --grey-light: #e3e3e3;
    --grey-mid: #d4d4d4;
  }
  * { box-sizing: border-box; margin: 0; padding: 0; }
  html, body { width: 1200px; height: 900px; overflow: hidden; }
  body {
    position: relative;
    background: var(--page);
    font-family: "Arimo", Arial, sans-serif;
    color: var(--ink);
  }
  .slide {
    position: absolute;
    width: 481px;
    height: 361px;
    background: var(--white);
    overflow: hidden;
    box-shadow: 0 2px 6px rgba(0,0,0,.18);
  }
  .slide--title   { left: 69px;  top: 38px; }
  .slide--section { left: 670px; top: 38px; }
  .slide--content { left: 60px;  top: 449px; }
  .slide--closing { left: 680px; top: 459px; }

  .brand {
    font-family: "Source Sans 3", "Myriad Pro", sans-serif;
    font-weight: 400;
    color: var(--cyan);
    white-space: nowrap;
  }

  /* title slide */
  .slide--title .brand {
    position: absolute; left: 0; right: 0; top: 133px;
    text-align: center; font-size: 31px; letter-spacing: .2px;
  }
  .deck-title {
    position: absolute; left: 0; right: 0; top: 216px;
    text-align: center; font-size: 21px; color: var(--ink-soft);
  }
  .deck-subtitle {
    position: absolute; left: 0; right: 0; top: 241px;
    text-align: center; font-size: 11.5px; color: var(--ink-soft);
  }

  /* section & closing slides */
  .stage {
    background: linear-gradient(180deg, #ffffff 0%, #ffffff 22%, #e6e6e6 60%, #e2e2e2 100%);
  }
  .stage__panel {
    position: absolute; left: 0; right: 0; bottom: 0;
    background: linear-gradient(180deg, #f4f4f4 0%, #e9e9e9 60%, #dcdcdc 100%);
    border-top: 1px solid #ececec;
  }
  .slide--section .stage__panel { top: 215px; }
  .slide--closing .stage__panel { top: 190px; }
  .bubbles {
    position: absolute; width: 112px; height: 62px;
    background:
      radial-gradient(circle at 50% 85%, rgba(30,160,215,.95) 0%, rgba(52,180,230,.75) 38%, rgba(120,205,240,.35) 62%, rgba(255,255,255,0) 75%);
  }
  .slide--section .bubbles { top: 153px; }
  .slide--closing .bubbles { top: 128px; }
  .bubbles--left { left: 6px; }
  .bubbles--right { right: 4px; }
  .stage__heading {
    position: absolute; left: 0; right: 0;
    text-align: center; font-weight: 700; font-size: 15px; color: var(--ink-soft);
  }
  .slide--section .stage__heading { top: 172px; }
  .slide--closing .stage__heading { top: 147px; }
  .thanks {
    position: absolute; left: 0; right: 0; top: 233px;
    text-align: center; font-size: 35px; color: var(--ink-soft);
  }

  /* content slide */
  .content-title {
    position: absolute; left: 55px; top: 26px;
    font-size: 15.5px; font-weight: 700; font-style: italic; color: #222;
  }
  .page-badge { position: absolute; left: 432px; top: 23px; width: 20px; height: 20px; }
  .feature-row { position: absolute; left: 43px; top: 70px; width: 360px; height: 72px; }
  .points-row {
    position: absolute; left: 41px; top: 176px;
    display: flex; width: 374px; height: 74px;
  }
  .points {
    flex: 1; list-style: none; padding: 10px 6px 0 10px;
    font-size: 8.5px; font-weight: 700; line-height: 13.5px;
    border: 2px solid rgba(0,0,0,.12);
  }
  .points li::before { content: "➢"; margin-right: 9px; font-size: 7px; }
  .points--slate  { background: var(--slate); color: #fff; }
  .points--cyan   { background: var(--cyan); color: #1b3a4a; border-color: var(--cyan-deep); }
  .points--yellow { background: var(--yellow); color: #4a4a3a; border-color: var(--yellow-edge); }
  .slide--content .brand {
    position: absolute; right: 11px; bottom: 31px; font-size: 14px;
  }
</style>
</head>
<body>

<section class="slide slide--title">
  <p class="brand">ClinicMeadowlane™</p>
  <h1 class="deck-title">Presentation title Here</h1>
  <p class="deck-subtitle">Presentation sub title here</p>
</section>

<section class="slide slide--section stage">
  <div class="stage__panel"></div>
  <div class="bubbles bubbles--left" role="img" aria-label="Cluster of blue bubbles"></div>
  <div class="bubbles bubbles--right" role="img" aria-label="Cluster of blue bubbles"></div>
  <h2 class="stage__heading">Your Section Title comes Here</h2>
</section>

<section class="slide slide--content">
  <h2 class="content-title">Your Content Slide comes here</h2>
  <svg class="page-badge" viewBox="0 0 20 20" aria-label="Slide 1">
    <polygon points="10,1 18,5.5 18,14.5 10,19 2,14.5 2,5.5" fill="#4d5055"/>
    <text x="10" y="13.5" text-anchor="middle" font-family="Arimo, sans-serif" font-size="9" font-weight="700" fill="#fff">1</text>
  </svg>

  <svg class="feature-row" viewBox="0 0 360 72">
    <g font-family="Arimo, sans-serif" font-weight="700" font-size="9.5" text-anchor="middle">
      <circle cx="34" cy="36" r="32" fill="#fff" stroke="#5a5d61" stroke-width="1.4"/>
      <circle cx="34" cy="38" r="17" fill="#8fd3ec" role="img" aria-label="Lab flask icon"/>
      <circle cx="89" cy="36" r="32" fill="var(--slate)" stroke="#3c4045" stroke-width="2"/>
      <circle cx="89" cy="36" r="29" fill="none" stroke="#7c8187" stroke-width="1"/>
      <text fill="#fff"><tspan x="89" y="25">Your</tspan><tspan x="89" y="39">Content</tspan><tspan x="89" y="53">here</tspan></text>

      <circle cx="151" cy="36" r="32" fill="#fff" stroke="#5a5d61" stroke-width="1.4"/>
      <circle cx="151" cy="38" r="17" fill="#3bb5e0" role="img" aria-label="Patient icon"/>
      <circle cx="206" cy="36" r="32" fill="var(--cyan)" stroke="#5a5d61" stroke-width="1.4"/>
      <circle cx="206" cy="36" r="29" fill="none" stroke="#6ecbea" stroke-width="1"/>
      <text fill="#1d5a78"><tspan x="206" y="25">Your</tspan><tspan x="206" y="39">Content</tspan><tspan x="206" y="53">here</tspan></text>

      <circle cx="268" cy="36" r="32" fill="#fff" stroke="#5a5d61" stroke-width="1.4"/>
      <circle cx="268" cy="38" r="17" fill="#f1b13a" role="img" aria-label="Awareness ribbon icon"/>
      <circle cx="324" cy="36" r="32" fill="var(--yellow)" stroke="#5a5d61" stroke-width="1.4"/>
      <circle cx="324" cy="36" r="29" fill="none" stroke="var(--yellow-edge)" stroke-width="1"/>
      <text fill="#4a4a3a"><tspan x="324" y="25">Your</tspan><tspan x="324" y="39">Content</tspan><tspan x="324" y="53">here</tspan></text>
    </g>
  </svg>

  <div class="points-row">
    <ul class="points points--slate"><li>Your Points here</li><li>Your Points here</li><li>Your Points here</li></ul>
    <ul class="points points--cyan"><li>Your Points here</li><li>Your Points here</li><li>Your Points here</li></ul>
    <ul class="points points--yellow"><li>Your Points here</li><li>Your Points here</li><li>Your Points here</li></ul>
  </div>

  <p class="brand">ClinicMeadowlane™</p>
</section>

<section class="slide slide--closing stage">
  <div class="stage__panel"></div>
  <div class="bubbles bubbles--left" role="img" aria-label="Cluster of blue bubbles"></div>
  <div class="bubbles bubbles--right" role="img" aria-label="Cluster of blue bubbles"></div>
  <h2 class="stage__heading">Closing slide comes here</h2>
  <p class="thanks">Thank you</p>
</section>

</body>
</html>
```